Business card design needed

partition walls
suspended ceilings
bulkheads
shops
office fitouts
compressed sheeting

main colour aqua blue with silver and white writing

Industry/Entity Type

Business

Contact Information for Business Card

k.m.r plastering (vic) pty.ltd

owen tarkley
M:0400716204 E:kmrplastering@mailnest.example
ABN: 63 402 917 548
ACN: 471 605 284

```html
<!DOCTYPE html>
<html lang="en">
<head>
<meta charset="utf-8">
<title>K.M.R Plastering business card</title>
<link rel="stylesheet" href="https://fonts.googleapis.com/css2?family=Open+Sans:wght@300;400;600;700&display=swap">
<style>
  :root {
    --page-bg: #2b2b2b;
    --aqua-deep: #0a7fc6;
    --aqua-mid: #1f8fd3;
    --aqua-light: #78bde6;
    --white: #ffffff;
    --text-shadow: rgba(0, 40, 90, 0.55);
    --photo-grey: #6b7785;
    --photo-warm: #9a8a86;
  }
  html, body {
    margin: 0;
    padding: 0;
    width: 1200px;
    height: 1000px;
    overflow: hidden;
    background: var(--page-bg);
    font-family: "Open Sans", Arial, sans-serif;
  }
  .business-card {
    position: absolute;
    left: 132px;
    top: 255px;
    width: 936px;
    height: 510px;
    overflow: hidden;
    background: radial-gradient(ellipse at 60% 45%, #2a9ce0 0%, var(--aqua-mid) 45%, var(--aqua-deep) 100%);
    color: var(--white);
  }
  .company-name {
    position: absolute;
    right: 15px;
    top: 12px;
    margin: 0;
    font-size: 35px;
    font-weight: 600;
    letter-spacing: -1px;
    text-shadow: 2px 2px 2px var(--text-shadow);
    white-space: nowrap;
  }
  .contact-band {
    position: absolute;
    left: 178px;
    top: 168px;
    width: 730px;
    height: 200px;
    background: linear-gradient(90deg, rgba(120,189,230,0) 0%, rgba(120,189,230,0.55) 25%, var(--aqua-light) 50%, rgba(120,189,230,0.55) 78%, rgba(120,189,230,0.15) 100%);
  }
  .trowel-photo {
    position: absolute;
    left: 20px;
    top: 105px;
    width: 310px;
    height: 405px;
    background: radial-gradient(ellipse at 50% 50%, var(--photo-grey) 0%, rgba(107,119,133,0.75) 40%, rgba(154,138,134,0.35) 65%, rgba(31,143,211,0) 100%);
  }
  .person-name {
    position: absolute;
    left: 421px;
    top: 218px;
    margin: 0;
    font-size: 35px;
    font-weight: 400;
    letter-spacing: -1px;
    text-shadow: 2px 2px 2px var(--text-shadow);
    white-space: nowrap;
  }
  .contact-line, .registration-line {
    position: absolute;
    margin: 0;
    font-size: 19px;
    font-weight: 400;
    text-shadow: 1px 1px 2px var(--text-shadow);
    white-space: nowrap;
    letter-spacing: -0.3px;
  }
  .contact-line b, .registration-line b { font-weight: 700; }
  .contact-phone { left: 469px; top: 273px; }
  .contact-email { left: 469px; top: 302px; }
  .registration-abn { left: 719px; top: 443px; }
  .registration-acn { left: 719px; top: 472px; }
</style>
</head>
<body>
  <div class="business-card">
    <div class="contact-band"></div>
    <div class="trowel-photo" role="img" aria-label="Photo of a hand holding a plastering trowel against a freshly plastered wall"></div>

    <h1 class="company-name">K.M.R PLASTERING (VIC) PTY.LTD</h1>

    <h2 class="person-name">OWEN TARKLEY</h2>
    <p class="contact-line contact-phone"><b>phone:</b> 0400716204</p>
    <p class="contact-line contact-email"><b>e-mail:</b> kmrplastering@mailnest.example</p>

    <p class="registration-line registration-abn"><b>ABN:</b> 63 402 917 548</p>
    <p class="registration-line registration-acn"><b>ACN:</b> 471 605 284</p>
  </div>
</body>
</html>
```